Marketing Flyer

I need a flyer for my marketing company. I would like for it to to be consistent with my logo and business card design. I would also like for there to be an image of a crowded waiting room, or restaurant with people gathered around a flat screen that reads "Your Ad Here".

• logo, info on attached doc.
• Possibly a picture people in a waiting room or restaurant with a digital sign present that reads "your ad here".

```html
<!DOCTYPE html>
<html lang="en">
<head>
<meta charset="utf-8">
<title>Benefits of Advertising with FieldSprout Marketing</title>
<link rel="stylesheet" href="https://fonts.googleapis.com/css2?family=Oswald:wght@500;700&family=Roboto+Condensed:wght@400;700&family=Montserrat:wght@800&family=Arimo&display=swap">
<style>
  :root {
    --green: #86c440;
    --grey: #646464;
    --ink: #1a1a1a;
    --white: #ffffff;
    --screen-frame: #1c1c1c;
  }
  * { margin: 0; padding: 0; box-sizing: border-box; }
  html, body { width: 927px; height: 1200px; overflow: hidden; background: var(--white); }
  .flyer { position: relative; width: 927px; height: 1200px; overflow: hidden; background: var(--white); }

  .top-band { position: absolute; left: 0; top: 0; width: 927px; height: 280px; background: var(--green); }

  .screen {
    position: absolute; left: 132px; top: 60px; width: 662px; height: 398px;
    background: var(--white); border: 8px solid var(--screen-frame); border-radius: 4px;
    box-shadow: 0 18px 30px rgba(0,0,0,0.12);
  }
  .screen-stand { position: absolute; left: 417px; top: 438px; }

  .headline { position: absolute; font-family: "Oswald", sans-serif; font-weight: 700; line-height: 1; text-transform: uppercase; white-space: nowrap; }
  .headline--benefits { left: 208px; top: 94px; font-size: 112px; color: var(--grey); letter-spacing: 0; }
  .headline--of { left: 674px; top: 158px; font-size: 42px; color: var(--grey); }
  .headline--advertising { left: 168px; top: 193px; font-size: 90px; color: var(--green); letter-spacing: -0.5px; }
  .headline--with { left: 666px; top: 236px; font-size: 44px; color: var(--grey); }

  .brand-name {
    position: absolute; left: 140px; top: 322px; width: 646px; text-align: center;
    font-family: "Roboto Condensed", sans-serif; font-weight: 700; font-size: 58px;
    color: var(--grey); line-height: 1;
  }

  .ad-bubble { position: absolute; left: 686px; top: 382px; }
  .ad-bubble__label {
    position: absolute; left: 686px; top: 437px; width: 126px; text-align: center;
    font-family: "Oswald", sans-serif; font-weight: 700; font-size: 18px; color: var(--ink);
  }

  .what-we-do { position: absolute; left: 0; top: 488px; width: 933px; text-align: center; }
  .what-we-do__title { font-family: "Oswald", sans-serif; font-weight: 700; font-size: 27px; color: var(--ink); line-height: 1.2; }
  .what-we-do__text { font-family: "Arimo", sans-serif; font-size: 20.5px; color: var(--ink); line-height: 35px; margin-top: -2px; }

  .benefits { position: absolute; left: 54px; top: 604px; width: 810px; list-style: none; font-family: "Roboto Condensed", sans-serif; font-size: 18.5px; color: var(--ink); }
  .benefit { display: flex; line-height: 24px; }
  .benefit__tag {
    flex: 0 0 146px; height: 21px; margin-top: 2px; padding-left: 9px; border-radius: 11px;
    background: var(--green); font-weight: 700; line-height: 21px; white-space: nowrap;
  }
  .benefit__colon { flex: 0 0 20px; text-align: center; font-weight: 700; }
  .benefit__text { flex: 1; }
  .benefit__text strong { font-weight: 700; }

  .audience-photo {
    position: absolute; left: 0; top: 852px; width: 927px; height: 348px;
    background: linear-gradient(180deg, #ffffff 0%, #d9c6b0 22%, #6b4e38 48%, #2b2b30 75%, #1e1e22 100%);
  }

  .slogan-band {
    position: absolute; left: 0; top: 1054px; width: 927px; height: 68px; background: var(--green);
    font-family: "Roboto Condensed", sans-serif; font-weight: 700; font-size: 32px; color: var(--ink);
    text-align: center; line-height: 68px;
  }

  .contact {
    position: absolute; left: 0; top: 1136px; width: 927px; text-align: center;
    font-family: "Montserrat", sans-serif; font-weight: 800; font-size: 19px; color: var(--white);
    letter-spacing: 0.5px; text-shadow: 0 1px 3px rgba(0,0,0,0.6);
  }
  .contact__divider { margin: 0 22px; }
</style>
</head>
<body>
<main class="flyer">
  <div class="top-band"></div>

  <div class="screen"></div>
  <svg class="screen-stand" width="82" height="14" viewBox="0 0 82 14" aria-hidden="true">
    <polygon points="12,0 70,0 82,14 0,14" fill="#1c1c1c"/>
  </svg>

  <div class="headline headline--benefits">Benefits</div>
  <div class="headline headline--of">of</div>
  <div class="headline headline--advertising">Advertising</div>
  <div class="headline headline--with">with</div>

  <div class="brand-name">FieldSprout Marketing</div>

  <svg class="ad-bubble" width="126" height="112" viewBox="0 0 126 112" aria-hidden="true">
    <polygon points="56,30 82,0 76,30" fill="var(--green)"/>
    <rect x="0" y="26" width="126" height="86" rx="6" fill="var(--green)"/>
  </svg>
  <div class="ad-bubble__label">Your Ad Here</div>

  <section class="what-we-do">
    <h2 class="what-we-do__title">WHAT WE DO</h2>
    <p class="what-we-do__text">WE DESIGN AN AD FOR YOUR COMPANY<br>AND PLACE IT ON THE TV AT LOCAL BUSINESSES.</p>
  </section>

  <ul class="benefits">
    <li class="benefit"><span class="benefit__tag">Inexpensive</span><span class="benefit__colon">:</span><span class="benefit__text">Only <strong>$31.00 per month!</strong></span></li>
    <li class="benefit"><span class="benefit__tag">Exposure</span><span class="benefit__colon">:</span><span class="benefit__text">Our digital signage is placed in only the best/high traffic businesses in your area.</span></li>
    <li class="benefit"><span class="benefit__tag">Repetition</span><span class="benefit__colon">:</span><span class="benefit__text">Your ad is shown over 3,500 time each month (42,000 times per year)!</span></li>
    <li class="benefit"><span class="benefit__tag">Local</span><span class="benefit__colon">:</span><span class="benefit__text">We show your ad to consumers in YOUR area. Let us help you do business with<br>the people you want to do business with.</span></li>
    <li class="benefit"><span class="benefit__tag">Exclusivity</span><span class="benefit__colon">:</span><span class="benefit__text">Only 2 ads per industry.</span></li>
    <li class="benefit"><span class="benefit__tag">Lead Generation</span><span class="benefit__colon">:</span><span class="benefit__text">We show consumers how to reach you and where to find you.</span></li>
    <li class="benefit"><span class="benefit__tag">Brand Awareness</span><span class="benefit__colon">:</span><span class="benefit__text">People need to know your business. We make that happen by putting your<br>brand right in front of them.</span></li>
    <li class="benefit"><span class="benefit__tag">Digital</span><span class="benefit__colon">:</span><span class="benefit__text">Digital advertising has higher retention rates and higher consumer engagement.</span></li>
  </ul>

  <div class="audience-photo" role="img" aria-label="Photo of a crowd of people seen from behind, looking up at a screen"></div>

  <div class="slogan-band">Let us make you famous in your community!</div>

  <p class="contact">CALL US NOW 555 014 2378<span class="contact__divider">|</span>www.fieldsprout.com</p>
</main>
</body>
</html>
```